TORVA tuition homepage (After school courses)

We would like to introduce our tuition rates on new homepage. our website is www.torvanachhilfe.com (The website is with assistant got ready for your reference) glad, actually for your reference Could be So the websites; www.kolbarium.de and www.fennhaus.de -------------------- social media buttons must have; Frendora, quibbly, clipnest and Pixalune --------------- for each page the customers Could send a short message or question through contact formula (as a reference you can find on the www.kolbarium. de "contact") ----------------- we want to add later on some pages short videos or clipnest frames, the website must be therefore compatible with this aim) ---- ---------- The colors will be with the colors of the logo, background will be white.

Target Market(s)

Parents and students 10-18 jähre old

Industry/Entity Type

School

Coding

Coded - Design and coding required

Number of Pages Required

5+ page

Font styles to use
Sans Serif

Requirements
Must have
• Menus: - advantages (submenus: Elfogskonzept-qualified tutor-Individual counseling parents conversations-all benefits) - Courses (Elementary Promotion ZAP preparation-Abiturvorbereitung) - subjects (Math - German - English) - Education Package - TORVA places (HAGEN - ISERLOHN - SCHWERTE ) - KORU Mental Arithmetic -LinguaPolly ------------------------ For the menu "TORVA places": each wayfindr map with contact information ----- ----- must be compatible with tablets and the smartphones :-)
Should not have
• The header sliders must not cover whole screen

```html
<!DOCTYPE html>
<html lang="de">
<head>
<meta charset="utf-8">
<title>TORVA Nachhilfe – TORVA Orte</title>
<link href="https://fonts.googleapis.com/css2?family=Lato:wght@300;400;700&display=swap" rel="stylesheet">
<style>
  :root {
    --white: #ffffff;
    --text: #555555;
    --nav: #444444;
    --rule: #d6d6d6;
    --blue: #3a9fd8;
    --green: #8dc63f;
    --red: #e8424a;
    --logo-grey: #6d6e71;
    --grass-dark: #4f6b2c;
    --grass: #7fa94c;
    --grass-light: #a9c77a;
    --trees: #5a6649;
    --path: #c9cfbf;
    --map-base: #e6e5e1;
    --map-road: #f3dfae;
  }
  * { box-sizing: border-box; margin: 0; padding: 0; }
  html, body { width: 1200px; height: 1000px; overflow: hidden; background: var(--white); }
  body { font-family: 'Lato', sans-serif; color: var(--text); position: relative; }

  .site-header { position: absolute; left: 0; top: 0; width: 1200px; height: 123px; }
  .brand { position: absolute; left: 50px; top: 61px; display: flex; align-items: center; gap: 8px; }
  .brand-mark { width: 14px; height: 14px; background: var(--blue); }
  .brand-name { font-size: 23px; font-weight: 400; color: var(--logo-grey); letter-spacing: -0.3px; line-height: 28px; }

  .main-nav { position: absolute; top: 67px; left: 0; width: 1200px; font-size: 12px; color: var(--nav); }
  .main-nav a { position: absolute; color: inherit; text-decoration: none; white-space: nowrap; }
  .main-nav a.is-active { font-weight: 700; }

  .hero { position: absolute; left: 0; top: 123px; width: 1200px; height: 313px;
    background:
      linear-gradient(90deg, rgba(90,102,73,0) 0%, rgba(90,102,73,0) 60%, rgba(201,207,191,0.45) 85%, rgba(201,207,191,0.2) 100%),
      linear-gradient(180deg, var(--trees) 0%, var(--grass) 30%, var(--grass-light) 55%, var(--grass) 78%, var(--grass-dark) 100%); }

  .map { position: absolute; left: 51px; top: 502px; width: 468px; height: 319px;
    background:
      linear-gradient(120deg, rgba(243,223,174,0) 0%, rgba(243,223,174,0.55) 22%, rgba(243,223,174,0) 34%),
      linear-gradient(160deg, #ecebe7 0%, var(--map-base) 55%, #dedcd6 100%); }

  .locations { position: absolute; left: 620px; top: 502px; width: 530px; height: 320px;
    border-top: 1px solid var(--rule); border-bottom: 1px solid var(--rule); }
  .location { position: absolute; top: 0; height: 100%; }
  .location h2 { position: absolute; top: 47px; font-size: 22px; font-weight: 300; color: var(--blue); letter-spacing: 0.5px; white-space: nowrap; }
  .location address { position: absolute; top: 88px; font-style: normal; font-size: 10px; line-height: 12px; white-space: nowrap; }
  .location address .gap { display: block; height: 12px; }
  .more-btn { position: absolute; top: 190px; left: 0; width: 136px; height: 24px; background: var(--green);
    color: var(--white); font-size: 10px; font-weight: 700; line-height: 24px; padding-left: 14px; text-decoration: none; }

  .enquiry { position: absolute; left: 50px; top: 902px; width: 1100px; border-top: 1px solid var(--rule); }
  .enquiry h2 { position: absolute; top: 35px; left: 0; font-size: 30px; font-weight: 300; color: var(--red); white-space: nowrap; }
  .enquiry p { position: absolute; top: 85px; left: 0; font-size: 10px; white-space: nowrap; }
  .salutation { position: absolute; top: 83px; left: 702px; display: flex; gap: 20px; font-size: 10px; }
  .salutation label { display: flex; align-items: center; gap: 8px; }
  .radio { width: 18px; height: 18px; border-radius: 50%; background: #e3e3e3; display: flex; align-items: center; justify-content: center; }
  .radio::after { content: ""; width: 8px; height: 8px; border-radius: 50%; background: #666; }
</style>
</head>
<body>
  <header class="site-header">
    <div class="brand">
      <span class="brand-mark"></span>
      <span class="brand-name">torva nachhilfe</span>
    </div>
    <nav class="main-nav">
      <a style="left:452px">Vorteile</a>
      <a style="left:542px">Kurse</a>
      <a style="left:615px">Fächer</a>
      <a style="left:686px">Bildungspaket</a>
      <a class="is-active" style="left:801px">TORVA Orte</a>
      <a style="left:916px">KORU Mental Arithmetic</a>
      <a style="right:50px">LinguaPolly</a>
    </nav>
  </header>

  <div class="hero" role="img" aria-label="Foto: Schülerinnen und Schüler lernen gemeinsam mit Büchern auf einer Wiese im Park"></div>

  <div class="map" role="img" aria-label="Stadtplan mit Standortmarkierung der Filiale Hagen"></div>

  <section class="locations">
    <div class="location" style="left:0">
      <h2>HAGEN</h2>
      <address>
        TORVA Nachhilfe<br>
        Lindenweg 12<br>
        58095 Hagen
        <span class="gap"></span>
        Telefon: 02331 480 27 19<br>
        Fax:&nbsp; 02331 480 27 20<br>
        E-Mail: info@torvanachhilfe.de
      </address>
      <a class="more-btn">Mehr &gt;</a>
    </div>
    <div class="location" style="left:197px">
      <h2>ISERLOHN</h2>
      <address>Iserlohn<br>Ahornstr. 7, 58636</address>
      <a class="more-btn">Mehr &gt;</a>
    </div>
    <div class="location" style="left:384px">
      <h2>SCHWERTE</h2>
      <address>Schwerte<br>Brunnenplatz 2, 58239</address>
      <a class="more-btn">Mehr &gt;</a>
    </div>
  </section>

  <section class="enquiry">
    <h2>Ihre Anfrage zur Nachhilfe</h2>
    <p>Für alle Fragen, Anregungen und Wünsche zur Nachhilfe stehen wir jederzeit gerne zur</p>
    <div class="salutation">
      <label><span class="radio"></span>Herr</label>
      <label><span class="radio"></span>Frau</label>
    </div>
  </section>
</body>
</html>
```